SkyVarro logo and website for a cloud solution provider in the UK market

Produce a logo with strong brand identity and a website themed similar to the log design.

The website is for a company called SkyVarro limited. SkyVarro specialises in migrating businesses from their on premise infrastructure to cloud services such as Deskwell365, Torvane and also Pelligrin Host Systems.

We offer migration and management services to allow customers to focus on their core business letting SkyVarro manage their business IT services and infratructure.

The design should leverage the Quillent partner information for the cost savings of migrating on premise solutions to the cloud. The website should also leverage Quillents content syndication to help with marketing materials and campaigns. the website links can be found here: https://setandrun.quillent-example.com

The website must be suitable for both desktop and mobile platforms including smartphones and tablets.

The design should communicate financial savings, confidence and user flexibility.

Reason: I need a website which will easy render on mobile devices which isn't too cluttered and has clear areas where I can insert Quillent syndicate banner content of sizes 180x150, 600x90 or 600x250. For details of Quillent syndicated content please see: http://setandrun.quillent-example.com

Target Market(s)

Small to medium companies who use on premise email, Filemesh, and web infrastructure who want to migrate their business safely to the cloud.

Industry/Entity Type

It Company

Logo Text

SkyVarro

Number of Pages Required

4 page

```html
<!DOCTYPE html>
<html lang="en">
<head>
<meta charset="utf-8">
<title>SkyVarro — Cloud Migration &amp; Management</title>
<link href="https://fonts.googleapis.com/css2?family=Open+Sans:wght@400;600;700&display=swap" rel="stylesheet">
<style>
  :root {
    --brand: #1d4f8f;
    --brand-dark: #163d70;
    --brand-light: #2c64aa;
    --ink: #2b2b2b;
    --muted: #6c6c6c;
    --accent: #c8312b;
    --page: #ffffff;
    --soft: #eef1f5;
    --footer: #1f2125;
    --footer-bar: #15171a;
    --footer-text: #b8bcc2;
  }
  * { box-sizing: border-box; margin: 0; padding: 0; }
  html, body { width: 759px; height: 1200px; overflow: hidden; }
  body { font-family: "Open Sans", Arial, sans-serif; color: var(--ink); background: var(--page); }

  .site-header { height: 62px; display: flex; align-items: center; justify-content: space-between; padding: 0 28px 0 30px; }
  .brand { font-size: 27px; font-weight: 600; color: var(--brand); letter-spacing: 0.2px; }
  .main-nav { display: flex; align-items: center; gap: 2px; }
  .main-nav a { font-size: 9px; font-weight: 600; color: var(--ink); text-decoration: none; padding: 8px 9px; text-transform: uppercase; }
  .main-nav a.is-active { background: var(--brand); color: #fff; padding: 8px 18px; }
  .search-btn { width: 24px; height: 24px; background: #8b8f96; margin-left: 8px; display: flex; align-items: center; justify-content: center; }

  .hero { height: 268px; background: linear-gradient(135deg, var(--brand-light) 0%, var(--brand) 55%, var(--brand-dark) 100%); position: relative; padding: 34px 0 0 70px; color: #fff; overflow: hidden; }
  .hero h1 { font-size: 24px; font-weight: 400; line-height: 1.2; width: 390px; }
  .hero p { font-size: 10px; line-height: 1.5; width: 220px; margin-top: 14px; }
  .btn-light { display: inline-block; background: #fff; color: var(--brand); font-size: 10px; font-weight: 700; padding: 9px 40px; margin-top: 16px; text-transform: uppercase; }
  .hero-art { position: absolute; right: 70px; top: 34px; width: 200px; height: 200px; border-radius: 50%; background: radial-gradient(circle, #e6e9ee 0%, #9fb1c8 60%, rgba(255,255,255,0) 72%); }

  .offer-bar { margin: 20px 28px 0; display: flex; align-items: center; justify-content: space-between; }
  .offer-bar h2 { background: var(--brand); color: #fff; font-size: 16px; font-weight: 400; padding: 9px 36px; width: 498px; }
  .btn-outline { border: 1px solid #cfd4da; font-size: 10px; font-weight: 700; padding: 11px 40px; text-transform: uppercase; color: var(--ink); background: #fff; }

  .services { display: flex; justify-content: space-between; margin: 24px 80px 0 86px; padding-bottom: 22px; border-bottom: 1px solid #e3e6ea; }
  .service { display: flex; gap: 10px; width: 170px; }
  .service svg { flex: none; }
  .service h3 { font-size: 10px; font-weight: 700; }
  .service p { font-size: 7px; color: var(--muted); line-height: 1.4; margin-top: 2px; }
  .service .more { font-size: 7px; color: var(--accent); font-weight: 600; }

  .portfolio { margin-top: 18px; height: 222px; background: linear-gradient(180deg, #fafbfc 0%, var(--soft) 100%); }
  .portfolio h2 { text-align: center; font-size: 20px; font-weight: 400; color: var(--brand); padding-top: 14px; letter-spacing: 0.5px; }
  .portfolio-rule { width: 230px; height: 1px; background: #cfd6df; margin: 6px auto 0; }
  .portfolio-grid { display: flex; height: 140px; margin-top: 20px; }
  .portfolio-item { flex: 1; }
  .item-laptop { background: linear-gradient(135deg, #c9ced4, #8a939d); }
  .item-feature { background: linear-gradient(135deg, #2a5d9e, #1b477f); display: flex; align-items: center; justify-content: center; }
  .item-cloud { background: linear-gradient(135deg, #d7dce1, #9aa3ad); }
  .btn-view { background: #fff; color: var(--brand); font-size: 8px; padding: 5px 12px; }

  .updates { display: flex; gap: 40px; margin: 24px 40px 0 70px; height: 214px; }
  .updates h2 { font-size: 14px; font-weight: 400; color: var(--ink); margin-bottom: 10px; }
  .news { width: 300px; }
  .news-item { display: flex; gap: 10px; margin-bottom: 12px; }
  .news-thumb { width: 60px; height: 40px; background: linear-gradient(135deg, #aab5c2, #5d6f85); flex: none; }
  .news-item h3 { font-size: 8px; font-weight: 700; }
  .news-item p, .news-item time { font-size: 7px; color: var(--muted); line-height: 1.35; display: block; }
  .testimonials { flex: 1; }
  .quote { display: flex; gap: 14px; margin-bottom: 18px; align-items: flex-start; }
  .avatar { width: 46px; height: 46px; border-radius: 50%; background: linear-gradient(135deg, #d4d8dd, #7e8792); flex: none; }
  .quote h3 { font-size: 8px; font-weight: 600; }
  .quote p { font-size: 7px; color: var(--muted); line-height: 1.4; }

  .site-footer { background: var(--footer); height: 182px; padding: 24px 40px 0 90px; display: flex; gap: 46px; color: var(--footer-text); }
  .site-footer h4 { font-size: 9px; color: #fff; font-weight: 600; text-transform: uppercase; margin-bottom: 10px; }
  .site-footer ul { list-style: none; }
  .site-footer li { font-size: 7px; line-height: 1.9; }
  .site-footer li::before { content: "›"; margin-right: 5px; }
  .newsletter p { font-size: 7px; margin-bottom: 8px; }
  .field { width: 110px; height: 16px; background: #fff; color: #888; font-size: 7px; padding: 3px 6px; margin-bottom: 6px; }
  .btn-send { display: inline-block; background: var(--brand); color: #fff; font-size: 8px; font-weight: 700; padding: 4px 22px; }
  .socials { display: flex; gap: 6px; margin-bottom: 18px; }
  .socials span { width: 14px; height: 14px; border-radius: 50%; background: #5c6168; }
  .footer-brand { font-size: 18px; font-weight: 600; color: #8d939b; }
  .copyright { background: var(--footer-bar); height: 22px; text-align: center; font-size: 7px; color: #8d939b; line-height: 22px; }
</style>
</head>
<body>
  <header class="site-header">
    <div class="brand">SkyVarro</div>
    <nav class="main-nav">
      <a class="is-active">Home</a><a>About Us</a><a>Services</a><a>Resources</a><a>Support</a><a>Contact</a>
      <span class="search-btn"><svg width="11" height="11" viewBox="0 0 12 12"><circle cx="5" cy="5" r="3.6" fill="none" stroke="#fff" stroke-width="1.5"/><line x1="7.7" y1="7.7" x2="11" y2="11" stroke="#fff" stroke-width="1.5"/></svg></span>
    </nav>
  </header>

  <section class="hero">
    <h1>Lorem Ipsum is simply dummy text of the printing and typesetting industry.</h1>
    <p>Lorem Ipsum is simply dummy text of the printing and typesetting industry. Lorem Ipsum has been the industry's standard dummy text ever since</p>
    <span class="btn-light">Read More</span>
    <div class="hero-art" role="img" aria-label="Illustration of connected cloud services and devices"></div>
  </section>

  <section class="offer-bar">
    <h2>We offer migration and management services</h2>
    <span class="btn-outline">Get Details</span>
  </section>

  <section class="services">
    <div class="service">
      <svg width="28" height="24" viewBox="0 0 28 24"><rect x="2" y="2" width="24" height="15" fill="none" stroke="#1d4f8f" stroke-width="2"/><line x1="14" y1="17" x2="14" y2="21" stroke="#1d4f8f" stroke-width="2"/><line x1="8" y1="22" x2="20" y2="22" stroke="#1d4f8f" stroke-width="2"/></svg>
      <div><h3>Pelligrin Host Systems</h3><p>Lorem Ipsum is simply dummy text of the printing</p><span class="more">Learn More</span></div>
    </div>
    <div class="service">
      <svg width="28" height="24" viewBox="0 0 28 24"><circle cx="14" cy="7" r="5" fill="#1d4f8f"/><path d="M4 23c0-6 4.5-9 10-9s10 3 10 9z" fill="#1d4f8f"/></svg>
      <div><h3>User Research</h3><p>Lorem Ipsum is simply dummy text of the printing</p><span class="more">Learn More</span></div>
    </div>
    <div class="service">
      <svg width="28" height="24" viewBox="0 0 28 24"><rect x="2" y="2" width="24" height="15" fill="none" stroke="#1d4f8f" stroke-width="2"/><rect x="10" y="17" width="8" height="3" fill="#1d4f8f"/><line x1="7" y1="22" x2="21" y2="22" stroke="#1d4f8f" stroke-width="2"/></svg>
      <div><h3>Deskwell365</h3><p>Lorem Ipsum is simply dummy text of the printing</p><span class="more">Learn More</span></div>
    </div>
  </section>

  <section class="portfolio">
    <h2>OUR PORTFOLIO</h2>
    <div class="portfolio-rule"></div>
    <div class="portfolio-grid">
      <div class="portfolio-item item-laptop" role="img" aria-label="Photo of hands typing on a laptop"></div>
      <div class="portfolio-item item-feature"><span class="btn-view">View portfolio</span></div>
      <div class="portfolio-item item-cloud" role="img" aria-label="Photo of a hand holding a glowing cloud"></div>
    </div>
  </section>

  <section class="updates">
    <div class="news">
      <h2>News Update</h2>
      <article class="news-item"><div class="news-thumb" role="img" aria-label="News photo"></div><div><h3>Lorem ipsum dolor sit amet,</h3><p>Lorem ipsum is simply dummy text of the printing and typesetting.</p><time>2 August, 2016 · 10 Comments</time></div></article>
      <article class="news-item"><div class="news-thumb" role="img" aria-label="News photo"></div><div><h3>Lorem ipsum dolor sit amet,</h3><p>Lorem ipsum is simply dummy text of the printing and typesetting.</p><time>2 August, 2016 · 10 Comments</time></div></article>
      <article class="news-item"><div class="news-thumb" role="img" aria-label="News photo"></div><div><h3>Lorem ipsum dolor sit amet,</h3><p>Lorem ipsum is simply dummy text of the printing and typesetting.</p><time>2 August, 2016 · 10 Comments</time></div></article>
    </div>
    <div class="testimonials">
      <h2>TESTIMONIALS</h2>
      <div class="quote"><div class="avatar" role="img" aria-label="Client portrait"></div><div><h3>Lorem Ipsum</h3><p>Lorem Ipsum is simply dummy text of the printing and typesetting industry. Lorem Ipsum has been the standard dummy text ever since.</p></div></div>
      <div class="quote"><div class="avatar" role="img" aria-label="Client portrait"></div><div><h3>Lorem Ipsum</h3><p>Lorem Ipsum is simply dummy text of the printing and typesetting industry. Lorem Ipsum has been the standard dummy text ever since.</p></div></div>
    </div>
  </section>

  <footer class="site-footer">
    <div><h4>Main Menu</h4><ul><li>Home</li><li>About us</li><li>Services</li><li>Resources</li><li>Support</li><li>Contact</li></ul></div>
    <div><h4>Quick Link</h4><ul><li>Company Policy</li><li>Our Policy</li><li>Terms and conditions of use</li><li>Secure payment</li><li>Sitemap</li></ul></div>
    <div class="newsletter"><h4>Newsletter</h4><p>Lorem ipsum dolor sit amet</p><div class="field">Your Name</div><div class="field">Email Id</div><span class="btn-send">SEND</span></div>
    <div><h4>Get in Touch</h4><div class="socials"><span></span><span></span><span></span><span></span></div><div class="footer-brand">SkyVarro</div></div>
  </footer>
  <div class="copyright">Copyright © 2016 SkyVarro. All Rights Reserved.</div>
</body>
</html>
```